Flicktor - photography in NYC - leveraging big data and robotics

We've got a photography business in NYC. It is kind of on-demand photographers, but actually is just five of us who work as a team. Over the last three years we've taken tens of thousands of photographs and are now sitting on a load of great work. We want to leverage that in a way that lets people book either by event type or location. So, they would click on Harrow Green and a load of examples of our work would pop up. Or Wedding Shower, and relevant examples would pop up. We've got the pictures structured pretty well to enable this. Now we just need a website that illustrates this and then leads through the booking process (time, location, date, contact etc.) and payment.

Target Market(s)

Everyone - corporates, real estate, tourists, families, headshots, bloggers, products, wedding showers, baby showers, engagements, venues, restaurants/bars, holiday pictures, Marlow Hall weddings, kids birthday parties, adult birthday parties, PR companies, corporate events.... long list.

Industry/Entity Type

Photographer

Number of Pages Required

5+ page

Colors

Designer to choose colors to be used in the design.

Requirements
Must have
• A great, engaging landing page which people can choose by event type or location. This would then pull in examples of our work in that location or in that event type. Then they go through the booking process. This is simple capturing key details - see here https://flicktorphoto.example/book/
Nice to have
• Social links
Should not have
• Nothing specific.

```html
<!DOCTYPE html>
<html lang="en">
<head>
<meta charset="utf-8">
<title>Flicktor – Book an Event</title>
<link rel="stylesheet" href="https://fonts.googleapis.com/css2?family=Figtree:wght@400;500;600;700;800&display=swap">
<style>
  :root {
    --ink: #111214;
    --muted: #8b8e93;
    --rule: #bfc2c6;
    --paper: #ffffff;
    --footer-bg: #f2f3f5;
    --accent: #e0401c;
    --photo-light: #dfe4e7;
    --photo-mid: #8e9195;
    --photo-dark: #2f3236;
  }
  * { box-sizing: border-box; margin: 0; padding: 0; }
  html, body { width: 1200px; height: 675px; overflow: hidden; background: var(--paper); }
  body { position: relative; font-family: "Figtree", sans-serif; color: var(--ink); }

  .site-header { position: absolute; left: 0; top: 0; width: 1200px; height: 52px; background: var(--paper); box-shadow: 0 1px 2px rgba(0,0,0,0.04); z-index: 2; }
  .brand { position: absolute; left: 37px; top: 14px; font-size: 15px; font-weight: 800; letter-spacing: -0.2px; text-transform: uppercase; }
  .search-icon { position: absolute; left: 987px; top: 27px; }
  .menu-toggle { position: absolute; left: 1038px; top: 30px; font-size: 7px; font-weight: 700; letter-spacing: 3px; }
  .menu-lines { position: absolute; left: 1076px; top: 31px; }

  .hero-photo { position: absolute; left: 540px; top: 52px; width: 660px; height: 559px;
    background:
      radial-gradient(ellipse 45% 45% at 58% 55%, var(--photo-dark) 0%, rgba(47,50,54,0.6) 55%, rgba(47,50,54,0) 100%),
      linear-gradient(to right, var(--paper) 0%, var(--paper) 12%, var(--photo-light) 38%, var(--photo-mid) 70%, var(--photo-dark) 100%); }

  .booking { position: absolute; left: 0; top: 52px; width: 1200px; height: 559px; z-index: 1; }
  .booking-title { position: absolute; left: 110px; width: 524px; top: 38px; text-align: center; font-size: 35px; font-weight: 700; letter-spacing: 0.3px; }
  .field { position: absolute; border-bottom: 1px solid var(--rule); height: 20px; }
  .field label { position: absolute; left: 0; bottom: 3px; font-size: 10.5px; font-weight: 500; }
  .submit-btn { position: absolute; left: 306px; top: 470px; width: 134px; height: 42px; border: 1px solid var(--ink); background: transparent; font-family: inherit; font-size: 13px; font-weight: 700; letter-spacing: 0.6px; color: var(--ink); }

  .site-footer { position: absolute; left: 0; top: 611px; width: 1200px; height: 64px; background: var(--footer-bg); font-size: 8px; }
  .footer-rule { position: absolute; left: 0; top: 36px; width: 63px; border-top: 1px solid #55585c; }
  .footer-about { position: absolute; left: 72px; top: 30px; font-size: 10.5px; }
  .social { position: absolute; top: 33px; width: 7px; height: 7px; border-radius: 50%; background: #3a3d41; }
  .footer-nav a { position: absolute; top: 32px; color: #3a3d41; text-decoration: none; }
  .footer-nav a.more { color: var(--accent); }
  .copyright { position: absolute; right: 110px; top: 32px; color: #a3a6aa; }
</style>
</head>
<body>
  <header class="site-header">
    <div class="brand">Flicktor</div>
    <svg class="search-icon" width="12" height="12" viewBox="0 0 12 12" aria-label="Search">
      <circle cx="5" cy="5" r="3.8" fill="none" stroke="#8b8e93" stroke-width="1.2"/>
      <line x1="7.8" y1="7.8" x2="11" y2="11" stroke="#8b8e93" stroke-width="1.2"/>
    </svg>
    <div class="menu-toggle">MENU</div>
    <svg class="menu-lines" width="15" height="6" viewBox="0 0 15 6" aria-hidden="true">
      <line x1="4" y1="1" x2="15" y2="1" stroke="#111214" stroke-width="1.2"/>
      <line x1="0" y1="5" x2="15" y2="5" stroke="#111214" stroke-width="1.2"/>
    </svg>
  </header>

  <div class="hero-photo" role="img" aria-label="Photographer holding a camera with a large lens up to his eye, fading into white on the left"></div>

  <main class="booking">
    <h1 class="booking-title">Event</h1>
    <div class="field" style="left:110px;top:118px;width:524px"><label>Event</label></div>
    <div class="field" style="left:110px;top:176px;width:524px"><label>Venue name</label></div>
    <div class="field" style="left:110px;top:233px;width:524px"><label>Street</label></div>
    <div class="field" style="left:110px;top:290px;width:256px"><label>City</label></div>
    <div class="field" style="left:378px;top:290px;width:256px"><label>State</label></div>
    <div class="field" style="left:110px;top:346px;width:524px"><label>Phone No</label></div>
    <div class="field" style="left:110px;top:403px;width:524px"><label>Email Address</label></div>
    <button class="submit-btn" type="button">SUBMIT</button>
  </main>

  <footer class="site-footer">
    <div class="footer-rule"></div>
    <div class="footer-about">About</div>
    <span class="social" style="left:126px" aria-label="Social link"></span>
    <span class="social" style="left:141px" aria-label="Social link"></span>
    <span class="social" style="left:160px" aria-label="Social link"></span>
    <nav class="footer-nav">
      <a href="#" style="left:212px">Corporates</a>
      <a href="#" style="left:282px">Property</a>
      <a href="#" style="left:341px">Tourists</a>
      <a href="#" style="left:398px">Headshots</a>
      <a href="#" style="left:464px">Bloggers</a>
      <a href="#" style="left:525px">Engagements</a>
      <a href="#" style="left:603px">Weddings</a>
      <a href="#" class="more" style="left:669px">+ More</a>
    </nav>
    <div class="copyright">©2018 Dana Flicktor. All Rights Reserved.</div>
  </footer>
</body>
</html>
```